Corlinden Rx pharmacy / Local Independent Pharmacy

we need a logo with ( our staff picture on it ) for hometown pharmacy who treated patients as family , encourage customers to transfer their prescriptions to our pharmacy, delivering their medications for free and we accept all/most Insurances

Industry/Entity Type

Pharmaceutical

Colors
0054AA
0677BA
7BADD7
CADEEF
E8F1F8
EB3D1F
EC4F4E
F09395
F8D3D4
FCEDEE

Requirements
Must have
• THE PICTURE FOR THE STAFF , I DOWNLOADED TO THE PROJECT

```html
<!DOCTYPE html>
<html lang="en">
<head>
<meta charset="utf-8">
<title>Corlinden Rx – Complete Pharmacy Needs</title>
<link href="https://fonts.googleapis.com/css2?family=Francois+One&family=Roboto:wght@500;700;900&display=swap" rel="stylesheet">
<style>
  :root {
    --blue-deep: #0054AA;
    --blue-mid: #0677BA;
    --blue-soft: #7BADD7;
    --blue-pale: #CADEEF;
    --blue-mist: #E8F1F8;
    --red: #EB3D1F;
    --red-soft: #EC4F4E;
    --white: #ffffff;
    --badge-navy: #12428f;
  }
  * { margin: 0; padding: 0; box-sizing: border-box; }
  html, body { width: 1200px; height: 444px; overflow: hidden; background: #ffffff; }
  .billboard {
    position: relative;
    width: 1200px;
    height: 444px;
    overflow: hidden;
    background: radial-gradient(ellipse at 62% 45%, var(--blue-soft) 0%, #3f86cc 45%, var(--blue-deep) 100%);
    font-family: "Roboto", Arial, sans-serif;
  }
  .billboard__shapes { position: absolute; inset: 0; }
  .headline {
    color: var(--white);
    font-family: "Francois One", "Arial Narrow", sans-serif;
    font-weight: 400;
    text-transform: uppercase;
    text-shadow: 0 3px 4px rgba(0, 30, 80, .35);
    line-height: 1;
  }
  .headline span { position: absolute; white-space: nowrap; }
  .headline__top { left: 622px; top: 14px; font-size: 36px; letter-spacing: 1px; }
  .headline__main { left: 596px; top: 40px; font-size: 112px; letter-spacing: 1px; }
  .headline__end { left: 952px; top: 146px; font-size: 34px; letter-spacing: 1px; }
  .phone-band {
    position: absolute;
    left: 548px;
    top: 205px;
    height: 74px;
    display: flex;
    align-items: center;
    gap: 26px;
    color: var(--white);
  }
  .phone-band__icon { width: 44px; height: 56px; }
  .phone-band__number { font-weight: 700; font-size: 52px; letter-spacing: 1px; line-height: 1; }
  .benefits {
    position: absolute;
    left: 462px;
    top: 282px;
    list-style: none;
    color: var(--white);
    font-size: 25px;
    font-weight: 500;
    letter-spacing: .8px;
    line-height: 39px;
  }
  .benefits li::before { content: "• "; }
  .free-badge { position: absolute; left: 1031px; top: 230px; width: 150px; height: 150px; }
  .free-badge__word {
    position: absolute; left: 0; right: 0; top: 38px;
    text-align: center; color: var(--white);
    font-family: "Francois One", sans-serif; font-size: 40px; line-height: 1;
  }
  .free-badge__ribbon {
    position: absolute; left: 18px; right: 18px; top: 86px;
    background: var(--red); color: var(--white);
    text-align: center; font-weight: 700; font-size: 19px; line-height: 26px;
  }
</style>
</head>
<body>
<main class="billboard">
  <svg class="billboard__shapes" width="1200" height="444" viewBox="0 0 1200 444">
    <defs>
      <linearGradient id="staffPhotoTone" x1="0" y1="0" x2="0" y2="1">
        <stop offset="0" stop-color="#c9ced3"/>
        <stop offset=".45" stop-color="#9aa39b"/>
        <stop offset="1" stop-color="#e9ecef"/>
      </linearGradient>
    </defs>
    <rect class="phone-band__bar" x="420" y="205" width="780" height="74" fill="var(--red)"/>
    <path class="staff-photo" role="img" aria-label="Photo of the three pharmacy staff members in white lab coats standing inside the pharmacy"
          d="M0 0 H440 Q500 150 430 444 H0 Z" fill="url(#staffPhotoTone)"/>
    <path class="staff-photo__edge" d="M440 0 Q500 150 430 444" fill="none" stroke="var(--red-soft)" stroke-width="16"/>
  </svg>

  <h1 class="headline">
    <span class="headline__top">Complete</span>
    <span class="headline__main">Pharmacy</span>
    <span class="headline__end">Needs</span>
  </h1>

  <div class="phone-band">
    <svg class="phone-band__icon" viewBox="0 0 44 56" aria-hidden="true">
      <rect x="20" y="4" width="4" height="50" fill="#fff"/>
      <circle cx="22" cy="6" r="4" fill="#fff"/>
      <path d="M20 12 Q6 8 2 14 Q10 16 20 18 Z M24 12 Q38 8 42 14 Q34 16 24 18 Z" fill="#fff"/>
      <path d="M22 20 C10 24 10 30 22 32 C34 34 34 40 22 44" fill="none" stroke="#fff" stroke-width="3"/>
    </svg>
    <span class="phone-band__number">(555) 014-2876</span>
  </div>

  <ul class="benefits">
    <li>We treat you as family.</li>
    <li>Easily transfer your prescription.</li>
    <li>We accept all/ most Insurances.</li>
  </ul>

  <div class="free-badge">
    <svg width="150" height="150" viewBox="0 0 150 150" aria-hidden="true">
      <rect x="30" y="30" width="90" height="90" rx="8" transform="rotate(45 75 75)" fill="var(--badge-navy)" stroke="#fff" stroke-width="4"/>
      <circle cx="66" cy="32" r="2.5" fill="#fff"/><circle cx="75" cy="32" r="2.5" fill="#fff"/><circle cx="84" cy="32" r="2.5" fill="#fff"/>
    </svg>
    <span class="free-badge__word">FREE</span>
    <span class="free-badge__ribbon">Delivery</span>
  </div>
</main>
</body>
</html>
```